Cedar Hall businesscard

We changed our name and logo, now we need new business cards.
3-4/72 Marlow Street Fernleigh 2199
www.cedarhall-example.org.au
info@cedarhall-example.org.au
Lorna-Jean Whitcombe
Senior Pastor
ph: 02 95874210

```html
<!DOCTYPE html>
<html lang="en">
<head>
<meta charset="utf-8">
<title>Cedar Hall business card</title>
<link rel="stylesheet" href="https://fonts.googleapis.com/css2?family=Arimo:wght@400&display=swap">
<style>
  :root {
    --backdrop: #e6e6e7;
    --card: #f8f8f8;
    --slate: #6f808f;
    --accent: #5a7c98;
    --ink: #2a2a2c;
    --ink-soft: #444548;
  }
  * { margin: 0; padding: 0; box-sizing: border-box; }
  html, body {
    width: 1200px;
    height: 900px;
    overflow: hidden;
    background: var(--backdrop);
    font-family: "Arimo", Arial, sans-serif;
  }
  .stage { position: relative; width: 1200px; height: 900px; }
  .card {
    position: absolute;
    width: 560px;
    height: 320px;
    background: var(--card);
    box-shadow: 0 2px 6px rgba(0,0,0,0.10), 0 10px 24px rgba(0,0,0,0.06);
  }
  .card--front { left: 90px; top: 100px; }
  .card--back { left: 550px; top: 480px; }

  .brand {
    position: absolute;
    display: flex;
    align-items: center;
    gap: 10px;
    color: var(--slate);
    font-weight: 400;
    letter-spacing: 0.04em;
    white-space: nowrap;
  }
  .brand__dot {
    width: 16px; height: 16px;
    border-radius: 50%;
    background: var(--slate);
  }
  .card--front .brand {
    left: 50%; top: 50%;
    transform: translate(-50%, -50%);
    font-size: 26px;
  }
  .card--back .brand {
    right: 30px; top: 40px;
    font-size: 20px;
  }
  .brand__dot--small { width: 13px; height: 13px; }

  .person { position: absolute; left: 30px; top: 170px; }
  .person__name { font-size: 19px; color: var(--ink); }
  .person__role { font-size: 13px; color: var(--accent); margin-top: 3px; }

  .contact {
    position: absolute;
    left: 30px; bottom: 24px;
    font-size: 10.5px;
    line-height: 1.7;
    color: var(--ink-soft);
    white-space: nowrap;
  }
  .contact__org, .contact__label { color: var(--accent); }
  .contact__sep { color: var(--accent); padding: 0 3px; }
</style>
</head>
<body>
<main class="stage">
  <section class="card card--front" aria-label="Business card front">
    <div class="brand"><span class="brand__dot"></span>Cedar Hall</div>
  </section>

  <section class="card card--back" aria-label="Business card back">
    <div class="brand"><span class="brand__dot brand__dot--small"></span>Cedar Hall</div>
    <div class="person">
      <p class="person__name">Lorna-Jean Whitcombe</p>
      <p class="person__role">Senior Pastor</p>
    </div>
    <div class="contact">
      <p><span class="contact__org">Cedar Hall</span>, 3-4/72 Marlow Street, Fernleigh 2199</p>
      <p><span class="contact__label">T</span>&nbsp; 02 9587 4210<span class="contact__sep">•</span><span class="contact__label">E</span> info@cedarhall-example.org.au<span class="contact__sep">•</span><span class="contact__label">W</span> www.cedarhall-example.org.au</p>
    </div>
  </section>
</main>
</body>
</html>
```